Card for modern wood artisan that builds log homes and timber frames.

Design a card with catchy imagery. With a quick list of things I build and services I offer.

I'd like an English side and a french side. I can provide the text.

I am basically a guy that builds log homes and timber frames , but I am very eco friendly oriented.

I use only eco friendly products to limit my carbon footprint.
I want the client to feel as if they are hiring a good smart builder.

I have been building for a while but just starting out to market myself out there , not just work for other companies. Starting
My own thing legitimately.

I am very conscientious, and I take care of the work I do. I am trying to bring a new age, modern feel to an old profession.

Reason: I am not completely satisfied with A model yet, looking for that masculin rustic artistic design that I havent completely found yet. Thank you for your sumbissions.

Target Market(s)

People looking to hire a builder to design and build their projects.
And contractors that want to hire a quality subcontractor for their jobs.

Industry/Entity Type

Construction

Contact Information for Business Card

I want my logo on it, that I had designed here.
And a list of services I provide.

With my phone number, website adress and Email.

Requirements
Must have
• Artful presentation,
• Eco friendly feel
• I love trees.

```html
<!DOCTYPE html>
<html lang="en">
<head>
<meta charset="utf-8">
<title>Timberloft Business Card</title>
<link rel="stylesheet" href="https://fonts.googleapis.com/css2?family=Archivo+Black&family=Oswald:wght@400;600&family=Roboto:wght@400;500&display=swap">
<style>
  :root {
    --backdrop: #1d1d1d;
    --card-black: #141414;
    --card-white: #fbfbfb;
    --gold: #e3a12b;
    --gold-deep: #c98a1c;
    --ink: #1a1a1a;
    --paper-text: #ffffff;
  }
  html, body {
    margin: 0;
    width: 1200px;
    height: 873px;
    overflow: hidden;
    background: var(--backdrop);
  }
  .card {
    position: absolute;
    left: 150px;
    top: 180px;
    width: 900px;
    height: 514px;
    overflow: hidden;
    box-shadow: 0 20px 40px rgba(0,0,0,0.6);
  }
  .card-shapes { position: absolute; inset: 0; }
  .holder-name {
    position: absolute; left: 40px; top: 58px; margin: 0;
    font: 400 30px/1 "Archivo Black", sans-serif;
    color: var(--paper-text); letter-spacing: 0.5px;
  }
  .holder-role {
    position: absolute; left: 40px; top: 94px; margin: 0;
    font: 400 16px/1 "Archivo Black", sans-serif;
    color: var(--gold); letter-spacing: 1px;
  }
  .contact-list {
    position: absolute; left: 60px; top: 206px; margin: 0; padding: 0;
    list-style: none;
    font: 500 23px/1 "Roboto", sans-serif; color: var(--ink);
  }
  .contact-list li { display: flex; align-items: center; gap: 14px; height: 32px; }
  .contact-icon { width: 24px; height: 24px; flex: none; }
  .services {
    position: absolute; left: 50px; top: 420px; margin: 0;
    font: 400 20px/1.4 "Roboto", sans-serif; color: var(--paper-text);
  }
  .tree-art {
    position: absolute; left: 560px; top: 40px; width: 300px; height: 450px;
    background: radial-gradient(ellipse at 50% 40%, var(--gold) 0%, var(--gold-deep) 55%, rgba(201,138,28,0) 72%);
  }
  .brand {
    position: absolute; left: 590px; top: 176px;
    display: flex; align-items: center; gap: 14px;
  }
  .brand-mark { width: 34px; height: 34px; background: var(--ink); }
  .brand-name {
    font: 600 50px/1 "Oswald", sans-serif; color: var(--ink); letter-spacing: 1px;
  }
  .brand-tagline {
    position: absolute; left: 638px; top: 240px; margin: 0;
    font: 400 20px/1 "Oswald", sans-serif; color: var(--ink); letter-spacing: 1px;
  }
</style>
</head>
<body>
  <section class="card">
    <svg class="card-shapes" viewBox="0 0 900 514" width="900" height="514">
      <rect class="base-black" width="900" height="514" fill="var(--card-black)"/>
      <polygon class="stripe-white" points="0,176 363,176 371,186 0,186" fill="var(--card-white)"/>
      <polygon class="band-gold" points="0,192 376,192 467,312 0,312" fill="var(--gold)"/>
      <polygon class="stripe-white" points="0,318 471,318 479,328 0,328" fill="var(--card-white)"/>
      <polygon class="panel-white" points="245,0 900,0 900,514 635,514" fill="var(--card-white)"/>
    </svg>

    <div class="tree-art" role="img" aria-label="Golden illustration of a tall tree with exposed roots"></div>

    <div class="brand">
      <span class="brand-mark"></span>
      <span class="brand-name">TIMBERLOFT</span>
    </div>
    <p class="brand-tagline">WOOD ARTISAN</p>

    <h1 class="holder-name">OWEN HALE</h1>
    <p class="holder-role">MANAGING DIRECTOR</p>

    <ul class="contact-list">
      <li>
        <svg class="contact-icon" viewBox="0 0 24 24"><rect width="24" height="24" fill="var(--ink)"/><path d="M6 9c0-2 2-3 6-3s6 1 6 3l-2 1-1-2H9L8 10 6 9zm2 2h8l1 7H7l1-7zm4 2a2 2 0 100 4 2 2 0 000-4z" fill="#fff"/></svg>
        <span>2614 5580 3172</span>
      </li>
      <li>
        <svg class="contact-icon" viewBox="0 0 24 24"><rect width="24" height="24" fill="var(--ink)"/><rect x="5" y="7" width="14" height="10" fill="none" stroke="#fff" stroke-width="1.6"/><path d="M5 7l7 6 7-6" fill="none" stroke="#fff" stroke-width="1.6"/></svg>
        <span>owenhale@timberloft.com</span>
      </li>
      <li>
        <svg class="contact-icon" viewBox="0 0 24 24"><rect width="24" height="24" fill="var(--ink)"/><circle cx="12" cy="12" r="7" fill="none" stroke="#fff" stroke-width="1.6"/><path d="M5 12h14M12 5c3 3 3 11 0 14M12 5c-3 3-3 11 0 14" fill="none" stroke="#fff" stroke-width="1.2"/></svg>
        <span>www.timberloft.com</span>
      </li>
    </ul>

    <p class="services">Log homes • Timber frames • Timber frames<br>Log homes • Timber frames</p>
  </section>
</body>
</html>
```